Corporate Travel Technology Company needs new Business Card design

We need a new business card design to reflect our re-branded company. Our company is called vendaXo (pronounced eureka) and we provide Business Intelligence and mobile travel management solutions for the corporate travel industry. Our multinational customers use our solutions to manage large travel budgets and frequent travellers, as well as to save money and reduce risk. We'd like to see designs that use the blue and green palette as well as our corporate logo (attached below). The design should communicate innovation, insight, forward thinking, contemporary, trusted.

Target Market(s)

Large multinational corporates and Travel Agencies.

Industry/Entity Type

Business

Contact Information for Business Card

Marguerite Tallis
Chief Executive
vendaXo
Phone number - +61 (0)2 8147 3092
Email address - marguerite.tallis@vendaxo.example
Mobile number - +61 (0)455 206 718
www.vendaxo.example

Font styles to use
Other font styles liked:
• Please use font as close to corporate logo as possible

Colors
0255a3
0393ce
00a990
33b8a4
33a6d7
3176b5

Requirements
Must have
• Please include the words;
• Mobile Travel Management
• Accelerating Travel Business Insights
• Use corporate logo - although icon can be stylised if needed

```html
<!DOCTYPE html>
<html lang="en">
<head>
<meta charset="utf-8">
<title>vendaXo business card</title>
<link rel="stylesheet" href="https://fonts.googleapis.com/css2?family=Quicksand:wght@400;500;700&family=Arimo:wght@700&display=swap">
<style>
  :root {
    --backdrop: #4a3440;
    --card-white: #ffffff;
    --card-teal: #0aa990;
    --ink-slate: #3f5a5c;
    --ink-white: #ffffff;
    --accent-blue: #1ba4e0;
    --faint-grey: #e6eaf2;
    --faint-teal: rgba(255,255,255,0.12);
  }
  * { margin: 0; padding: 0; box-sizing: border-box; }
  html, body {
    width: 1200px; height: 800px; overflow: hidden;
    background: var(--backdrop);
  }
  .canvas {
    position: relative; width: 1200px; height: 800px;
    display: flex; align-items: center; justify-content: center; gap: 50px;
  }
  .card {
    position: relative; width: 520px; height: 297px; overflow: hidden;
    border-radius: 3px; box-shadow: 0 14px 30px rgba(0,0,0,0.35);
  }

  /* Front */
  .card-front { background: var(--card-white); }
  .card-front .backdrop-circle {
    position: absolute; right: -40px; top: 30px; width: 260px; height: 260px;
    border-radius: 50%; border: 22px solid var(--faint-grey);
  }
  .card-front .wordmark {
    position: absolute; left: 90px; top: 88px;
    font-family: "Quicksand", sans-serif; font-weight: 500;
    font-size: 76px; letter-spacing: -1px; color: var(--ink-slate);
  }
  .card-front .taglines {
    position: absolute; left: 92px; top: 200px;
    font-family: "Arimo", sans-serif; font-weight: 700;
    font-size: 15px; line-height: 1.35; color: var(--ink-slate);
  }
  .card-front .taglines p:first-child { padding-left: 30px; }

  /* Back */
  .card-back { background: var(--card-teal); color: var(--ink-white); }
  .card-back .backdrop-circle {
    position: absolute; right: 50px; top: -10px; width: 250px; height: 250px;
    border-radius: 50%; border: 24px solid var(--faint-teal);
  }
  .card-back .wordmark {
    position: absolute; right: 40px; top: 48px;
    font-family: "Quicksand", sans-serif; font-weight: 500;
    font-size: 64px; letter-spacing: -1px; color: var(--ink-white);
  }
  .card-back .person {
    position: absolute; left: 30px; top: 40px;
    font-family: "Quicksand", sans-serif;
  }
  .card-back .person-name {
    font-weight: 700; font-size: 17px; letter-spacing: 0.3px; text-transform: uppercase;
  }
  .card-back .person-role { font-size: 12px; margin-top: 8px; }
  .card-back .person-company { font-size: 11px; margin-top: 2px; }
  .card-back .divider {
    position: absolute; left: 30px; right: 40px; top: 150px;
    height: 2px; background: var(--ink-white);
  }
  .card-back .contacts {
    position: absolute; right: 40px; top: 170px; list-style: none;
    font-family: "Quicksand", sans-serif; font-weight: 500; font-size: 15px;
  }
  .card-back .contacts li {
    display: flex; align-items: center; gap: 10px; height: 23px;
  }
  .card-back .contacts svg {
    width: 14px; height: 14px; flex: none;
  }
</style>
</head>
<body>
<main class="canvas">

  <section class="card card-front" aria-label="Business card front">
    <div class="backdrop-circle" aria-hidden="true"></div>
    <div class="wordmark">vendaXo</div>
    <div class="taglines">
      <p>Mobile Travel Management</p>
      <p>Accelerating Travel Business Insights</p>
    </div>
  </section>

  <section class="card card-back" aria-label="Business card back">
    <div class="backdrop-circle" aria-hidden="true"></div>
    <div class="wordmark">vendaXo</div>
    <div class="person">
      <p class="person-name">Marguerite Tallis</p>
      <p class="person-role">Chief Executive</p>
      <p class="person-company">vendaXo</p>
    </div>
    <div class="divider"></div>
    <ul class="contacts">
      <li>
        <svg viewBox="0 0 14 14" aria-hidden="true"><rect width="14" height="14" rx="2" fill="#1ba4e0"/><path d="M4 3.5c.5-.4 1-.3 1.3.2l.6 1c.2.4 0 .7-.3 1l-.4.3c.4.9 1 1.6 1.9 2l.3-.4c.3-.3.6-.4 1-.2l1 .6c.5.3.5.8.1 1.3-.6.7-1.4.8-2.3.3C5.4 8.8 4.5 7.6 3.9 6 3.5 5 3.5 4 4 3.5z" fill="#fff"/></svg>
        <span>+61 (0)2 8147 3092</span>
      </li>
      <li>
        <svg viewBox="0 0 14 14" aria-hidden="true"><rect width="14" height="14" rx="2" fill="#1ba4e0"/><rect x="4.5" y="2.5" width="5" height="9" rx="1" fill="#fff"/><rect x="5.5" y="3.7" width="3" height="5" fill="#1ba4e0"/></svg>
        <span>+61 (0)455 206 718</span>
      </li>
      <li>
        <svg viewBox="0 0 14 14" aria-hidden="true"><rect width="14" height="14" rx="2" fill="#1ba4e0"/><rect x="3" y="4" width="8" height="6" fill="#fff"/><path d="M3 4l4 3.2L11 4" stroke="#1ba4e0" stroke-width="1" fill="none"/></svg>
        <span>marguerite.tallis@vendaxo.example</span>
      </li>
      <li>
        <svg viewBox="0 0 14 14" aria-hidden="true"><rect width="14" height="14" rx="2" fill="#1ba4e0"/><circle cx="7" cy="7" r="4" stroke="#fff" stroke-width="1.2" fill="none"/><path d="M3 7h8M7 3c-1.6 2.4-1.6 5.6 0 8M7 3c1.6 2.4 1.6 5.6 0 8" stroke="#fff" stroke-width="0.9" fill="none"/></svg>
        <span>www.vendaxo.example</span>
      </li>
    </ul>
  </section>

</main>
</body>
</html>
```